Apartment Investor Business Card Design

Need a new business card designed for my multifamily investment company

Industry/Entity Type

Real Estate

Contact Information for Business Card

Garrick Pelham - President & CEO
Brightwold Holdings, LLC
4838 North 92nd Avenue, Ste 500
Omaha, NE 68999
(402) 555-0147
Garrick@brightwoldholdings.example
Www.BrightwoldHoldings.example

Colors
3176b5

```html
<!DOCTYPE html>
<html lang="en">
<head>
<meta charset="utf-8">
<title>Brightwold Holdings – Business Card</title>
<link href="https://fonts.googleapis.com/css2?family=Cinzel:wght@400&family=Open+Sans:wght@400;700&display=swap" rel="stylesheet">
<style>
  :root {
    --backdrop: #3b3b3d;
    --card: #1e1e1f;
    --card-edge: #262627;
    --brand-blue: #3176b5;
    --blue-light: #4a87c9;
    --silver: #b9babd;
    --silver-dark: #8a8b8e;
    --white: #f2f2f2;
    --divider: #6d6d70;
    --band-grey: #8c8c8e;
  }
  * { margin: 0; padding: 0; box-sizing: border-box; }
  html, body { width: 1200px; height: 895px; overflow: hidden; }
  body { background: var(--backdrop); position: relative; font-family: "Open Sans", sans-serif; }

  .card {
    position: absolute;
    width: 600px; height: 343px;
    border-radius: 16px;
    background: linear-gradient(160deg, var(--card-edge), var(--card) 60%);
    box-shadow: 0 10px 30px rgba(0,0,0,.45);
    overflow: hidden;
  }
  .card--front { left: 70px; top: 80px; }
  .card--back  { left: 530px; top: 470px; }

  /* Front */
  .front-mark {
    position: absolute; inset: 0;
    display: flex; align-items: center; justify-content: center; gap: 14px;
  }
  .front-mark__square { width: 18px; height: 18px; background: var(--silver-dark); }
  .front-mark__name {
    font-family: "Cinzel", serif; font-weight: 400;
    font-size: 34px; letter-spacing: 1px; color: var(--silver);
  }

  /* Back */
  .back-mark {
    position: absolute; left: 26px; top: 0; width: 250px; height: 300px;
    display: flex; align-items: center; justify-content: center; gap: 10px;
  }
  .back-mark__square { width: 14px; height: 14px; background: var(--brand-blue); flex: none; }
  .back-mark__name {
    font-family: "Cinzel", serif; font-size: 22px; color: var(--white);
    line-height: 1.2; text-align: left;
  }
  .divider {
    position: absolute; left: 292px; top: 62px; width: 1px; height: 190px;
    background: var(--divider);
  }
  .details { position: absolute; left: 312px; top: 58px; right: 14px; color: var(--white); }
  .details__name {
    font-family: "Cinzel", serif; font-size: 20px; color: var(--blue-light); line-height: 1.1;
  }
  .details__title { font-size: 12.5px; margin-top: 3px; }
  .details__company { font-size: 13px; font-weight: 700; color: var(--blue-light); margin-top: 14px; }
  .details__address { font-size: 12px; line-height: 1.45; margin-top: 2px; }
  .contact-list { list-style: none; margin-top: 12px; }
  .contact-list li { display: flex; align-items: center; gap: 8px; font-size: 11.5px; line-height: 1.75; }
  .contact-list svg { width: 12px; height: 12px; flex: none; fill: var(--blue-light); }

  .bottom-band { position: absolute; left: 0; right: 0; bottom: 0; height: 9px; display: flex; }
  .bottom-band__blue { width: 56%; background: var(--brand-blue); }
  .bottom-band__grey { flex: 1; background: var(--band-grey); }
</style>
</head>
<body>

<section class="card card--front" aria-label="Card front">
  <div class="front-mark">
    <span class="front-mark__square"></span>
    <span class="front-mark__name">BRIGHTWOLD HOLDINGS</span>
  </div>
</section>

<section class="card card--back" aria-label="Card back">
  <div class="back-mark">
    <span class="back-mark__square"></span>
    <span class="back-mark__name">BRIGHTWOLD<br>HOLDINGS</span>
  </div>

  <div class="divider"></div>

  <div class="details">
    <div class="details__name">GARRICK PELHAM</div>
    <div class="details__title">President &amp; CEO</div>
    <div class="details__company">Brightwold Holdings, LLC</div>
    <div class="details__address">4838 North 92nd Avenue, Ste 500<br>Omaha, NE 68999</div>
    <ul class="contact-list">
      <li>
        <svg viewBox="0 0 24 24" aria-hidden="true"><path d="M6.6 10.8a15.1 15.1 0 0 0 6.6 6.6l2.2-2.2a1 1 0 0 1 1-.25 11.4 11.4 0 0 0 3.6.57 1 1 0 0 1 1 1V20a1 1 0 0 1-1 1A17 17 0 0 1 3 4a1 1 0 0 1 1-1h3.5a1 1 0 0 1 1 1c0 1.25.2 2.45.57 3.57a1 1 0 0 1-.25 1z"/></svg>
        (402) 555-0147
      </li>
      <li>
        <svg viewBox="0 0 24 24" aria-hidden="true"><path d="M2 5h20v14H2zm2 2v.5l8 5 8-5V7l-8 5z"/></svg>
        Garrick@brightwoldholdings.example
      </li>
      <li>
        <svg viewBox="0 0 24 24" aria-hidden="true"><path d="M12 2a10 10 0 1 0 0 20 10 10 0 0 0 0-20zm-1 2.1V8H7.3A8 8 0 0 1 11 4.1zm2 0A8 8 0 0 1 16.7 8H13zM4.5 10H11v4H4.5a8 8 0 0 1 0-4zm8.5 0h6.5a8 8 0 0 1 0 4H13zM7.3 16H11v3.9A8 8 0 0 1 7.3 16zm5.7 0h3.7a8 8 0 0 1-3.7 3.9z"/></svg>
        Www.BrightwoldHoldings.example
      </li>
    </ul>
  </div>

  <div class="bottom-band">
    <span class="bottom-band__blue"></span>
    <span class="bottom-band__grey"></span>
  </div>
</section>

</body>
</html>
```